Wordpress Design for my Consulting Company

We want a WordPress site created for our new business. We have created a mock-up of the content we want on the site at https://marcusdellow.example-sites.com/website-5

We are not attached to any of the pictures and just put stock stuff from wix's editor, which we don't have rights to use outside of wix.

We are NOT looking to just port this site to WordPress, we are looking for some creative ways to display the content in a more professional artistic sense.

I have included several logo files and a text file with the colors and Fonts used in the logo. We are not looking to change the logo or the colors used in the logo.

The Schedule appointment links to a page that embeds a bookingnest.example.com calendar. https://bookingnest.example.com/marcus-dellow/brightvale

The final website domain will be enterprisebrightvale.example

Enterprise brightvale is a consulting company that works directly with the business owners and leaders of small businesses between 50-200 employees. We help companies make sure they have the right technology to meet their strategic goals. We are the anti-"Computer Guy" and we focus on business outcomes NOT cool technology gadgets.

The final design should communicate business growth and success.

Target Market(s)

Business Owners of companies with 50-200 employees

Coding

Coded - Design and coding required

Number of Pages Required

1 page

Font styles to use
Serif
Other font styles liked:
• Trajan Pro Bold, Open Sans

Requirements
Must have
• Should focus on consulting rather than technology.
• Should show the customer as the hero and we are just their guide.
• Must use the logo provided and the colors and fonts in the text file provided. Any other colors and fonts must be complementary.
• The design should scale for all devices computer, iPad, or phone
Should not have
• Should not focus on technology, we are the anti-"Computer Guy" and we focus on business outcomes NOT cool technology gadgets.

```html
<!DOCTYPE html>
<html lang="en">
<head>
<meta charset="utf-8">
<title>Enterprise Brightvale — Technology Advisors That Get Business</title>
<link rel="stylesheet" href="https://fonts.googleapis.com/css2?family=Cinzel:wght@700&family=Montserrat:wght@400;600;700&family=Open+Sans:wght@400;600;700&display=swap">
<style>
:root{
  --slate:#3d4a52;
  --slate-dark:#2f3a41;
  --orange:#c97c50;
  --orange-deep:#b86d43;
  --grey:#5b5b5b;
  --grey-box:#6f6f6f;
  --footer:#333333;
  --white:#ffffff;
  --ink:#2a3338;
  --muted:#7a7a7a;
  --line:#d9d9d9;
  --yellow:#f5a623;
}
*{box-sizing:border-box;margin:0;padding:0}
html,body{width:1200px;height:3659px;overflow:hidden}
body{font-family:"Open Sans",Arial,sans-serif;color:var(--ink);background:var(--white);position:relative}
section,header,footer,.topbar{position:absolute;left:0;width:1200px}
.brand{display:flex;align-items:center;gap:14px;font-family:"Cinzel",Georgia,serif;font-weight:700;font-size:30px;letter-spacing:1px}
.brand-dot{width:34px;height:34px;border-radius:50%;background:var(--orange)}
.btn{display:inline-block;background:var(--orange);color:var(--white);font-family:"Montserrat",Arial,sans-serif;font-weight:600;font-size:15px;padding:11px 20px;border-radius:4px;text-decoration:none}
h2{font-family:"Montserrat",Arial,sans-serif;font-weight:700}

/* top bar & header */
.topbar{top:0;height:22px;background:var(--slate-dark);color:#e4e4e4;font-size:12px;text-align:center;line-height:22px}
.site-header{top:22px;height:83px;background:var(--white);display:flex;align-items:center;padding:0 120px}
.site-header .brand{color:var(--slate)}
.main-nav{margin-left:auto;display:flex;gap:34px;align-items:center;font-family:"Montserrat",Arial,sans-serif;font-size:14px;font-weight:600}
.main-nav a{color:var(--slate);text-decoration:none}
.main-nav a.active{color:var(--orange)}
.main-nav .btn{margin-left:24px;padding:11px 18px;font-size:14px}

/* hero */
.hero{top:105px;height:427px;background:linear-gradient(100deg,#d9d4cc 0%,#b7aea3 30%,#6f6a66 55%,#34393d 100%)}
.hero-copy{position:absolute;left:122px;top:100px;color:var(--white)}
.hero-copy h1{font-family:"Montserrat",Arial,sans-serif;font-weight:700;font-size:34px;line-height:1.15;color:#1d2428}
.hero-copy p{font-size:17px;line-height:1.3;margin:10px 0 18px;color:#1d2428;width:430px}

/* schedule */
.schedule{top:532px;height:212px;background:linear-gradient(90deg,#4b5359 0%,#6e6862 45%,#c27b52 100%);text-align:center;color:var(--white)}
.schedule h2{font-size:27px;margin-top:28px}
.days{display:flex;justify-content:center;align-items:center;gap:15px;margin-top:18px}
.day{width:63px;height:63px;border-radius:50%;border:2px solid var(--white);display:flex;flex-direction:column;justify-content:center;font-family:"Montserrat",Arial,sans-serif}
.day b{font-size:14px}.day span{font-size:11px}
.arrow{width:30px;height:30px}
.schedule p{font-family:"Montserrat",Arial,sans-serif;font-weight:600;font-size:15px;margin-top:14px}

/* gets */
.gets{top:744px;height:451px;text-align:center}
.gets h2{font-size:26px;color:var(--slate);margin-top:30px;letter-spacing:.5px}
.gets .lead{font-size:14px;color:var(--muted);margin-top:8px}
.benefit-row{position:absolute;top:124px;left:120px;display:flex;gap:8px}
.benefit{width:234px;height:234px;background:var(--slate);border-radius:4px;color:var(--white);display:flex;flex-direction:column;align-items:center;padding-top:32px}
.benefit.alt{background:var(--orange)}
.benefit .art{width:92px;height:92px;border-radius:50%;background:rgba(255,255,255,.22)}
.benefit h3{font-family:"Montserrat",Arial,sans-serif;font-size:18px;line-height:1.2;margin-top:20px}
.slider-dots{position:absolute;top:394px;left:580px;display:flex;gap:6px}
.slider-dots i{width:18px;height:6px;border-radius:3px;background:var(--slate)}
.slider-dots i+i{background:var(--orange)}

/* tired */
.tired{top:1195px;height:451px;background:var(--grey);color:var(--white);text-align:center}
.tired h2{font-size:28px;margin-top:62px}
.pain-grid{position:absolute;left:122px;top:125px;display:grid;grid-template-columns:repeat(3,312px);grid-auto-rows:120px;gap:12px 11px}
.pain{background:var(--grey-box);display:flex;align-items:center;justify-content:center;padding:0 40px;font-size:16px;line-height:1.3}

/* testimonials */
.voices{top:1646px;height:481px}
.voices .intro{position:absolute;left:220px;width:760px;top:42px;text-align:center;font-family:"Montserrat",Arial,sans-serif;font-size:18px;line-height:1.4;color:var(--ink)}
.quote{position:absolute;top:151px;width:467px;height:269px;border-radius:8px;background:var(--slate);color:var(--white);padding:38px 55px 0 68px}
.quote.alt{background:var(--orange)}
.quote p{font-size:16px;line-height:1.35}
.quote .mark{position:absolute;font-family:Georgia,serif;font-size:90px;line-height:1;color:rgba(255,255,255,.18)}
.quote .who{position:absolute;left:45px;bottom:-10px;display:flex;align-items:center;gap:20px}
.avatar{width:104px;height:104px;border-radius:50%;border:4px solid var(--white);background:linear-gradient(135deg,#9a8c80,#5c534d)}
.who b{display:block;font-family:"Montserrat",Arial,sans-serif;font-size:18px}
.who span{font-size:14px}

/* mindset */
.mindset{top:2127px;height:402px;background:linear-gradient(90deg,#f3f3f1 0%,#eceae6 38%,#8a8580 62%,#3b3f45 100%)}
.mindset-copy{position:absolute;left:122px;top:122px;width:420px}
.mindset-copy p{font-family:"Montserrat",Arial,sans-serif;font-size:17px;line-height:1.35;color:#4a4a4a}
.btn-outline{display:inline-block;margin-top:24px;border:2px solid var(--orange);color:var(--orange);font-family:"Montserrat",Arial,sans-serif;font-weight:600;font-size:13px;padding:9px 16px;border-radius:20px}

/* contact */
.contact{top:2529px;height:295px}
.contact h2{font-size:17px;color:var(--ink)}
.form-col{position:absolute;left:158px;top:62px;width:460px}
.fields{display:grid;grid-template-columns:222px 222px;gap:15px 14px;margin-top:22px}
.field{height:36px;border:1px solid var(--line);border-radius:3px;font-size:12px;color:#a3a3a3;padding:0 12px;line-height:34px}
.submit{height:36px;background:var(--orange);color:var(--white);border-radius:3px;text-align:center;line-height:36px;font-size:14px;width:142px;justify-self:end}
.ready-col{position:absolute;left:693px;top:62px}
.ready-col ul{list-style:none;margin-top:20px}
.ready-col li{display:flex;gap:10px;font-size:13px;line-height:1.25;margin-bottom:10px;width:320px}
.ready-col li svg{flex:none;margin-top:2px}
.call{font-family:"Montserrat",Arial,sans-serif;font-weight:700;font-size:17px;margin-top:8px}

/* steps */
.steps{top:2824px;height:449px;background:var(--orange);color:var(--white);text-align:center}
.steps .kicker{font-size:15px;margin-top:58px}
.steps h2{font-size:29px;line-height:1.25;margin-top:12px}
.step{position:absolute;top:212px;width:210px;text-align:center}
.step svg{display:block;margin:0 auto}
.step h3{font-family:"Montserrat",Arial,sans-serif;font-size:18px;margin-top:14px}
.step p{font-size:14px;line-height:1.3;margin-top:10px;color:#fbe8dc}

/* footer */
.site-footer{top:3273px;height:386px;background:var(--footer);color:#e6e6e6}
.site-footer .brand{position:absolute;left:122px;top:96px;color:var(--white)}
.footer-about{position:absolute;left:441px;top:73px;width:705px;font-size:12px;line-height:1.45}
.footer-contact{position:absolute;left:122px;top:186px;list-style:none;font-size:12px}
.footer-contact li{display:flex;align-items:center;gap:14px;margin-bottom:15px}
.footer-contact b{font-weight:700}
.subscribe{position:absolute;left:441px;top:182px;width:400px}
.subscribe h4{font-family:"Montserrat",Arial,sans-serif;font-size:15px}
.subscribe p{font-size:11px;line-height:1.4;margin-top:6px;width:360px}
.sub-form{display:flex;margin-top:12px}
.sub-form .input{width:303px;height:36px;background:var(--white);color:#999;font-size:12px;line-height:36px;padding:0 12px}
.sub-form .go{width:68px;height:36px;background:var(--yellow);color:var(--white);font-size:12px;line-height:36px;text-align:center}
.social{position:absolute;left:907px;top:193px;display:flex;gap:9px}
.social i{width:28px;height:28px;border:2px solid #cfcfcf;border-radius:3px}
.copyright{position:absolute;left:441px;top:303px;font-size:11px}
</style>
</head>
<body>

<div class="topbar">The Official Consumer Guide To Business Advisors in USA</div>

<header class="site-header">
  <div class="brand"><span class="brand-dot"></span>Brightvale</div>
  <nav class="main-nav">
    <a class="active" href="#">HOME</a><a href="#">ABOUT US</a><a href="#">SERVICES</a><a href="#">CONTACT US</a>
    <a class="btn" href="#">SCHEDULE APPOINTMENT</a>
  </nav>
</header>

<section class="hero" role="img" aria-label="Photo of a business leader silhouetted at a window overlooking a city skyline at sunrise">
  <div class="hero-copy">
    <h1>TECHNOLOGY ADVISORS<br>THAT "GET" BUSINESS.</h1>
    <p>We help you leverage technology to create a competitive advantage.</p>
    <a class="btn" href="#">Schedule Appointment</a>
  </div>
</section>

<section class="schedule">
  <h2>Schedule Appointment</h2>
  <div class="days">
    <svg class="arrow" viewBox="0 0 30 30"><path d="M18 8l-7 7 7 7" fill="none" stroke="#fff" stroke-width="2"/></svg>
    <div class="day"><b>Mon</b><span>Nov 26</span></div>
    <div class="day"><b>Tue</b><span>Nov 27</span></div>
    <div class="day"><b>Wed</b><span>Nov 28</span></div>
    <div class="day"><b>Thu</b><span>Nov 29</span></div>
    <div class="day"><b>Fri</b><span>Nov 30</span></div>
    <div class="day"><b>Sat</b><span>Dec 1</span></div>
    <svg class="arrow" viewBox="0 0 30 30"><path d="M12 8l7 7-7 7" fill="none" stroke="#fff" stroke-width="2"/></svg>
  </div>
  <p>Select Date and Schedule your Appointment</p>
</section>

<section class="gets">
  <h2>ENTERPRISE BRIGHTVALE GET</h2>
  <p class="lead">Neque porro quisquam est qui dolorem ipsum quia dolor sit amet, consectetur</p>
  <div class="benefit-row">
    <div class="benefit"><div class="art" role="img" aria-label="Illustration of an alarm clock"></div><h3>Reducing Time<br>to Decision</h3></div>
    <div class="benefit alt"><div class="art" role="img" aria-label="Illustration of a storefront"></div><h3>Preparing for<br>Disruption</h3></div>
    <div class="benefit"><div class="art" role="img" aria-label="Illustration of a handshake"></div><h3>Eliminating<br>Bottlenecks</h3></div>
    <div class="benefit"><div class="art" role="img" aria-label="Illustration of a customer service team"></div><h3>Standardizing<br>Customer Experience</h3></div>
  </div>
  <div class="slider-dots"><i></i><i></i></div>
</section>

<section class="tired">
  <h2>ARE YOU TIRED OF "COMPUTER GUYS" THAT...</h2>
  <div class="pain-grid">
    <div class="pain">Don't want to be involved in business strategy.</div>
    <div class="pain">Give you the excuse, "You never asked."</div>
    <div class="pain">Say "No!" but do not give options on how to achieve your business outcome.</div>
    <div class="pain">Recommend technology when a simple process or policy change would have the same effect.</div>
    <div class="pain">Can't explain how a technology will create business value, but insist it is necessary.</div>
    <div class="pain">Suggest expensive solutions that are just thrown away, soon after they are deployed.</div>
  </div>
</section>

<section class="voices">
  <p class="intro">We get the frustration of working with consultants and experts who don't listen or take the time to understand your company goals and vision. We believe technology should serve your business, not the other way around.</p>
  <div class="quote" style="left:122px">
    <span class="mark" style="left:16px;top:20px">&ldquo;</span>
    <p>"I knew I was behind, I just didn't know by how much. We had years of band-aided solutions and Brightvale helped us stabilize our environment and position ourselves to compete in the quickly changing world of copy and print"</p>
    <span class="mark" style="right:20px;bottom:-10px">&rdquo;</span>
    <div class="who"><div class="avatar" role="img" aria-label="Portrait photo of Dale Whitcombe"></div><div><b>Dale Whitcombe</b><span>Print Harbor</span></div></div>
  </div>
  <div class="quote alt" style="left:610px">
    <span class="mark" style="left:16px;top:20px">&ldquo;</span>
    <p>"Owen and the team at Brightvale are in all our strategy meetings whether or not we think technology will be discussed. And, they have brought great insight to better let us meet our goals.</p>
    <span class="mark" style="right:20px;bottom:-10px">&rdquo;</span>
    <div class="who"><div class="avatar" role="img" aria-label="Portrait photo of Reed Halloway"></div><div><b>Reed Halloway</b><span>Maple Grove Fellowship</span></div></div>
  </div>
</section>

<section class="mindset" role="img" aria-label="Photo of two smiling businessmen reviewing work at a laptop">
  <div class="mindset-copy">
    <p>Computer guys frustrate business leaders because they don't have a business mindset. Brightvale advises on strategy that helps companies apply technology to gain a competitive advantage.</p>
    <span class="btn-outline">Schedule Appointment</span>
  </div>
</section>

<section class="contact">
  <div class="form-col">
    <h2>NEED A BRIGHTVALE BUSINESS SERVICE?</h2>
    <div class="fields">
      <div class="field">Your Full Name</div><div class="field">Email</div>
      <div class="field">Reason For Selling*</div><div class="field">Estimated Property Value*</div>
      <div class="field">Business Address*</div><div class="submit">Submit</div>
    </div>
  </div>
  <div class="ready-col">
    <h2>WE'RE READY! Let's Discuss.</h2>
    <ul>
      <li><svg width="12" height="12" viewBox="0 0 12 12"><path d="M1 6l3 3 7-7" fill="none" stroke="#2a3338" stroke-width="2"/></svg>The standard Lorem Ipsum passage Finibus Bonorum et Malorum</li>
      <li><svg width="12" height="12" viewBox="0 0 12 12"><path d="M1 6l3 3 7-7" fill="none" stroke="#2a3338" stroke-width="2"/></svg>The standard Lorem Ipsum passage</li>
      <li><svg width="12" height="12" viewBox="0 0 12 12"><path d="M1 6l3 3 7-7" fill="none" stroke="#2a3338" stroke-width="2"/></svg>Finibus Bonorum et Malorum</li>
    </ul>
    <p class="call">Call Us Today: 000 000 0000</p>
  </div>
</section>

<section class="steps">
  <p class="kicker">Lorem Lism</p>
  <h2>The Four Steps to Aligning Technology<br>to your Business Strategy!</h2>
  <div class="step" style="left:136px">
    <svg width="64" height="64" viewBox="0 0 64 64" fill="none" stroke="#fff" stroke-width="2.5"><path d="M6 32c8-12 18-18 26-18s18 6 26 18c-8 12-18 18-26 18S14 44 6 32z"/><circle cx="32" cy="32" r="9"/></svg>
    <h3>Discover</h3><p>Identify what is going on behind the scenes, and create a snapshot of the current infrastructure.</p>
  </div>
  <div class="step" style="left:373px">
    <svg width="64" height="64" viewBox="0 0 64 64" fill="none" stroke="#fff" stroke-width="2.5"><circle cx="32" cy="14" r="8"/><circle cx="14" cy="48" r="8"/><circle cx="50" cy="48" r="8"/><path d="M28 21l-10 20M36 21l10 20M22 48h20"/></svg>
    <h3>Prioritize</h3><p>Meet to decide which solutions and policies will have the greatest impact on reaching the companies goals.</p>
  </div>
  <div class="step" style="left:619px">
    <svg width="64" height="64" viewBox="0 0 64 64" fill="none" stroke="#fff" stroke-width="2.5"><circle cx="32" cy="32" r="24"/><circle cx="32" cy="32" r="10"/><path d="M32 8v8M32 48v8M8 32h8M48 32h8"/></svg>
    <h3>Implement</h3><p>Implement those things that will give the greatest return on investment.</p>
  </div>
  <div class="step" style="left:858px">
    <svg width="64" height="64" viewBox="0 0 64 64" fill="none" stroke="#fff" stroke-width="2.5"><path d="M12 12l40 40M52 12L12 52"/><circle cx="12" cy="12" r="6"/><circle cx="52" cy="12" r="6"/></svg>
    <h3>Maintain</h3><p>Create a system that keeps your technology aligned as strategy adjusts over time.</p>
  </div>
</section>

<footer class="site-footer">
  <div class="brand"><span class="brand-dot"></span>Brightvale</div>
  <p class="footer-about">We sit beside owners and leadership teams to turn plans into results. Every recommendation starts with your business goals, your people and your budget, never with the latest gadget. We map where you are, agree on what matters most, deliver the changes that pay back fastest and keep everything aligned as your strategy grows.</p>
  <ul class="footer-contact">
    <li><svg width="14" height="18" viewBox="0 0 14 18"><path d="M7 1a6 6 0 016 6c0 5-6 10-6 10S1 12 1 7a6 6 0 016-6z" fill="#fff"/><circle cx="7" cy="7" r="2" fill="#333"/></svg><span><b>Brightvale Enterprise</b><br><br>12 LANTERN ROW, EASTBROOK</span></li>
    <li><svg width="14" height="14" viewBox="0 0 14 14"><path d="M3 1l3 3-2 2c1 2 2 3 4 4l2-2 3 3-2 2C6 13 1 8 1 3z" fill="#fff"/></svg>000-000-0000</li>
    <li><svg width="14" height="12" viewBox="0 0 14 12"><rect x="1" y="1" width="12" height="10" fill="none" stroke="#fff" stroke-width="1.5"/><path d="M1 1l6 5 6-5" fill="none" stroke="#fff" stroke-width="1.5"/></svg>hello@enterprisebrightvale.example</li>
  </ul>
  <div class="subscribe">
    <h4>Subscribe to our VIP List</h4>
    <p>Growing your business and short on time? Subscribers get early notice of new guides, events and practical advice for leaders.</p>
    <div class="sub-form"><div class="input">Email Address*</div><div class="go">Submit</div></div>
  </div>
  <div class="social"><i></i><i></i><i></i><i></i></div>
  <p class="copyright">Copyright © 2018 Brightvale Enterprise. All Rights Reserved</p>
</footer>

</body>
</html>
```